Open your window, widen your path PowerPoint Design Project

I would like up to 150 PPT slides created, that I can interchange depending on what I am presenting. Additional work beyond this brief will be to create workbooks based on these slides, which may be a direct replica of the slide.
The slides need to be professional but more importantly convey the playful, warm and human spirit we facilitate. I would love them to be gorgeous, professional, yet playful, and convey positive emotions so people smile when they see it. I love photographic images, white space, and would prefer them not looking all the same. Some slides will be animated.
I would also like them to have an OLV feel about them, so using my logo is one option, or including some reference to the logo.
I have the slides ready to go in terms of words, but will need images sourced and a template created.
The work we do is about building mindsets and behaviours that build emotional intelligence, trust, work/life balance, and some of the work we do is quite deep. I'm up for images that can be playful as well as those that could be more reflective.
I would love to see one or two pages as soon as possible but would need about 50 of them by 28th June - and another 25 or so by July 4. The rest I can wait till end of June if need be.
As this is a large project I am willing to negotiate additional payment with the selected designer, for this and ongoing work.

```html
<!DOCTYPE html>
<html lang="en">
<head>
<meta charset="utf-8">
<title>Observer Created Reality – OLV</title>
<link rel="stylesheet" href="https://fonts.googleapis.com/css2?family=Oswald:wght@600&family=Arimo:wght@400;700&family=Crimson+Text:ital@1&family=Carlito&display=swap">
<style>
  :root {
    --green-deep: #1e5a12;
    --green-band: #2f6b1f;
    --green-title: #3a9a1c;
    --green-bright: #3aa61e;
    --green-light: #8cc63f;
    --green-pale: #e8f3dc;
    --green-wash: #f4f9ee;
    --grey-text: #6a6a6a;
    --grey-rule: #9a9a9a;
    --band-grey: #ececec;
    --white: #ffffff;
  }
  * { box-sizing: border-box; margin: 0; padding: 0; }
  html, body { width: 1200px; height: 900px; overflow: hidden; background: var(--white); }
  .slide { position: relative; width: 1200px; height: 900px; overflow: hidden; background: var(--white); font-family: "Arimo", Arial, sans-serif; }

  .header { position: absolute; left: 0; top: 0; width: 1200px; height: 185px;
    background: linear-gradient(180deg, var(--white) 0%, var(--green-wash) 55%, var(--green-pale) 100%); }
  .header-waves { position: absolute; left: 0; top: 0; }
  .header-mark { position: absolute; left: 70px; top: 22px; width: 86px; height: 86px; border-radius: 50%;
    border: 3px solid var(--green-light); }
  .brand-name { position: absolute; right: 34px; top: 26px; font-family: "Arimo", Arial, sans-serif; font-weight: 400;
    font-size: 56px; letter-spacing: 1px; color: var(--green-bright); }

  .slide-title { position: absolute; left: 42px; top: 204px; font-family: "Oswald", "Arial Narrow", sans-serif; font-weight: 600;
    font-size: 33px; line-height: 1; color: var(--green-title); text-transform: uppercase; letter-spacing: 0.2px; }
  .title-rule { position: absolute; left: 42px; top: 246px; width: 1122px; height: 1px; background: var(--grey-rule); }

  .steps { position: absolute; left: 504px; top: 261px; width: 194px; list-style: none; }
  .step { height: 66px; margin-bottom: 11px; border-radius: 4px; border: 1px solid #c9dfba;
    background: linear-gradient(180deg, #fbfdf8 0%, #e4f0d8 60%, #cfe4bd 100%);
    box-shadow: 0 2px 4px rgba(0,0,0,0.18), inset 0 1px 0 var(--white);
    display: flex; align-items: center; justify-content: center;
    font-family: "Arimo", Arial, sans-serif; font-weight: 700; font-size: 38px; color: var(--green-deep); }

  .maintained { position: absolute; left: 0; top: 489px; width: 1200px; height: 46px;
    background: linear-gradient(180deg, #f6f6f6 0%, var(--band-grey) 100%);
    border-top: 1px solid #dcdcdc; border-bottom: 1px solid #dcdcdc; }
  .maintained-label { position: absolute; left: 45px; top: 11px; font-weight: 700; font-size: 22px; color: var(--green-deep); }
  .filter { position: absolute; top: 12px; font-size: 24px; color: var(--grey-text); padding-left: 26px; line-height: 1; }
  .filter::before { content: ""; position: absolute; left: 0; top: 6px; width: 13px; height: 13px; border-radius: 50%; background: var(--green-deep); }

  .footer-band { position: absolute; left: 0; top: 847px; width: 1200px; height: 53px;
    background: linear-gradient(180deg, var(--green-band) 0%, var(--green-deep) 100%); }

  .quote-disc { position: absolute; left: 430px; top: 537px; width: 340px; height: 340px; border-radius: 50%;
    background: radial-gradient(circle at 50% 35%, #4fae2a 0%, #2f8d18 55%, #1f6e0e 100%);
    border: 4px solid var(--white); box-shadow: 0 2px 10px rgba(0,0,0,0.35);
    display: flex; flex-direction: column; align-items: center; text-align: center; color: var(--white); z-index: 2; }
  .quote-text { margin-top: 26px; font-family: "Crimson Text", Georgia, serif; font-style: italic; font-size: 24px; line-height: 39px; }
  .quote-author { margin-top: 4px; font-family: "Carlito", Calibri, sans-serif; font-style: normal; font-size: 22px; line-height: 1.2; }
  .quote-source { margin-top: 4px; font-family: "Carlito", Calibri, sans-serif; font-style: italic; font-size: 13px; }

  .page-number { position: absolute; left: 1083px; top: 845px; width: 48px; height: 42px; border-radius: 9px;
    background: var(--white); border: 2px solid var(--green-deep); z-index: 3;
    display: flex; align-items: center; justify-content: center; font-weight: 700; font-size: 22px; color: #333; }
</style>
</head>
<body>
<main class="slide">
  <header class="header">
    <svg class="header-waves" width="1200" height="185" viewBox="0 0 1200 185" aria-hidden="true">
      <path d="M0 112 C 250 112, 500 92, 750 102 S 1050 150, 1200 130" fill="none" stroke="#2f9a3a" stroke-width="2.5"/>
      <path d="M0 128 C 300 120, 600 90, 850 98 S 1100 84, 1200 88" fill="none" stroke="#8cc63f" stroke-width="3"/>
      <path d="M0 140 C 350 138, 650 150, 900 118 S 1100 90, 1200 96" fill="none" stroke="#6f9d2f" stroke-width="2"/>
      <path d="M0 158 C 400 150, 700 130, 950 140 S 1120 150, 1200 146" fill="none" stroke="#b9d98a" stroke-width="2"/>
    </svg>
    <div class="header-mark" aria-hidden="true"></div>
    <div class="brand-name">OLV</div>
  </header>

  <h1 class="slide-title">Observer Created Reality</h1>
  <div class="title-rule"></div>

  <ol class="steps">
    <li class="step">SEE</li>
    <li class="step">DO</li>
    <li class="step">GET</li>
  </ol>

  <section class="maintained">
    <span class="maintained-label">Maintained by:</span>
    <span class="filter" style="left:255px">Distortion</span>
    <span class="filter" style="left:510px">Deletion</span>
    <span class="filter" style="left:723px">Invention</span>
    <span class="filter" style="left:942px">Generalisation</span>
  </section>

  <div class="footer-band"></div>

  <blockquote class="quote-disc">
    <p class="quote-text">The way our<br>brain is wired, we only<br>see what we believe is<br>possible. We match patterns<br>that already exist within<br>ourselves through conditioning.</p>
    <cite class="quote-author">Dr. Helena Marsh</cite>
    <span class="quote-source">Patterns of Feeling</span>
  </blockquote>

  <div class="page-number">09</div>
</main>
</body>
</html>
```